Velmo (Pathways for company scale) website

My plan is to offer a marketplace where by businesses (SME and Corporates) are able to post specific requirements, be that debt funding advice or other types of advice (legal/accountant) on the velmo website and advisors can seek to 'pitch' to the client.

clients should be anonymous - maybe a specific client number? (this is reduces the risk of bypass) and have the ability to choose the advisor via the advisors profile.

Advisors could potential use there Netlyne profile to auto complete on Velmo - not sure if this is possible or costs involved, however this would be ideal.

I would think Wordpress would be the best platform for this type of platform, however I would be guided by the experts.

I would need any code written in html 5 to allow for various devices (mobile, tablets, desktop)

Logo design is currently being completed also via Sketch Hive and I'm finalising colours ext now, so could provide advice in due course.

additional requirements (medium to longer term)
longer term I would be looking to add addition aspects to the site including algorithms, specific financial calculations, some of which I would be able to complete myself.

similar websites would be:
https://www.taskquill.example.au
http://www.fundoraxi.example.au

Industry/Entity Type

Debt

Coding

Coded - Design and coding required

```html
<!DOCTYPE html>
<html lang="en">
<head>
<meta charset="utf-8">
<title>Velmo — Pathways for company scale</title>
<link rel="stylesheet" href="https://fonts.googleapis.com/css2?family=Open+Sans:wght@300;400;600&family=Great+Vibes&display=swap">
<style>
:root{
  --teal:#1e6f7c;
  --teal-dark:#175864;
  --teal-band:#3f8d9a;
  --teal-quote:#2f7f8b;
  --teal-foot:#2b7a86;
  --ink:#2a2a2a;
  --muted:#8a8a8a;
  --line:#2f7f8b;
  --white:#ffffff;
  --grey-logo:#a5a5a5;
}
*{box-sizing:border-box;margin:0;padding:0}
html,body{width:1200px;height:3249px;overflow:hidden}
body{position:relative;background:var(--white);font-family:"Open Sans",Arial,sans-serif;color:var(--ink)}
.abs{position:absolute}

/* header */
.site-header{position:absolute;left:0;top:0;width:1200px;height:100px;background:var(--white)}
.brand{position:absolute;left:160px;top:10px;font-family:"Great Vibes",cursive;font-size:62px;color:var(--teal-dark);line-height:1}
.main-nav{position:absolute;left:602px;top:0;height:100px;display:flex}
.nav-item{width:76px;height:100px;display:flex;flex-direction:column;align-items:center;justify-content:center;font-size:10px;text-transform:uppercase;color:var(--ink);gap:8px}
.nav-item.active{background:var(--teal);color:var(--white);width:54px}
.nav-item svg{width:28px;height:28px}
.nav-search{width:60px;height:100px;display:flex;align-items:center;justify-content:center}

/* hero */
.hero{position:absolute;left:0;top:100px;width:1200px;height:470px;background:linear-gradient(90deg,#c9d6dc 0%,#e8eef1 35%,#d9d6d2 55%,#bfcdd6 80%,#9fb4c2 100%)}
.hero-title{position:absolute;left:160px;top:135px;font-size:44px;font-weight:400;line-height:52px;color:#23303a}
.hero-title .accent{color:var(--teal)}
.hero-sub{position:absolute;left:162px;top:252px;font-size:16px;color:#23303a}
.hero-btn{position:absolute;left:160px;top:299px;width:212px;height:52px;background:var(--teal);color:var(--white);font-size:15px;font-weight:600;display:flex;align-items:center;justify-content:center}
.hero-arrow{position:absolute;top:214px;width:48px;height:46px;background:#555c60;display:flex;align-items:center;justify-content:center}
.hero-progress{position:absolute;left:160px;top:466px;width:204px;height:4px;background:var(--teal)}

/* section titles */
.section-title{position:absolute;left:0;width:1200px;text-align:center;font-size:20px;text-transform:uppercase;color:var(--ink)}
.divider{position:absolute;left:160px;width:880px;height:2px;background:var(--line)}
.divider-badge{position:absolute;left:586px;width:28px;height:28px;border-radius:50%;background:var(--teal);display:flex;align-items:center;justify-content:center}
.on-dark .section-title{color:var(--white)}

/* services */
.service{position:absolute;top:748px;width:220px;text-align:center}
.service-icon{width:66px;height:66px;margin:0 auto;border:3px solid var(--teal);border-radius:50%;display:flex;align-items:center;justify-content:center}
.service-icon.filled{background:var(--teal)}
.service h3{margin-top:24px;font-size:13px;font-weight:600;text-transform:uppercase;color:var(--ink)}
.service p{margin-top:4px;font-size:11px;line-height:16px;color:var(--muted)}

/* stats */
.stats{position:absolute;left:0;top:962px;width:1200px;height:149px;background:linear-gradient(180deg,#4f98a4 0%,#3a8795 60%,#2f7886 100%)}
.stat{position:absolute;top:28px;width:200px;text-align:center;color:var(--white)}
.stat strong{display:block;font-size:56px;font-weight:300;line-height:62px}
.stat span{display:block;font-size:12px;text-transform:uppercase;letter-spacing:.5px}

/* work */
.work-tile{position:absolute;width:273px;height:174px}
.work-overlay{position:absolute;inset:0;background:rgba(20,30,35,.45)}
.zoom{position:absolute;left:120px;top:52px}
.work-label{position:absolute;left:28px;top:115px;width:245px;height:43px;background:#111;color:var(--white);font-size:12px;text-transform:uppercase;display:flex;align-items:center;justify-content:center}

/* testimonials */
.testimonials{position:absolute;left:0;top:1800px;width:1200px;height:425px;background:linear-gradient(180deg,#2c7c88 0%,#347f8b 55%,#2b737f 100%)}
.avatar{position:absolute;left:277px;top:189px;width:86px;height:86px;border-radius:50%;border:4px solid var(--white);background:radial-gradient(circle at 45% 40%,#e9d2b4,#c79a6b 70%)}
.quote{position:absolute;left:381px;top:209px;width:616px;font-size:11.5px;line-height:17px;color:var(--white)}
.quote-arrow{position:absolute;top:218px}
.dots{position:absolute;left:570px;top:339px;display:flex;gap:5px}
.dot{width:11px;height:11px;border-radius:50%;background:var(--white)}
.dot.hollow{background:transparent;border:2px solid var(--white)}

/* clients */
.client{position:absolute;top:2460px;display:flex;align-items:center;gap:10px;font-size:26px;font-weight:600;color:var(--grey-logo)}
.client-mark{width:34px;height:34px;border-radius:50%;background:#c3c3c3}
.client-arrow{position:absolute;top:2466px}

/* footer */
.site-footer{position:absolute;left:0;top:2615px;width:1200px;height:634px;background:linear-gradient(180deg,#2f8290 0%,#2a7885 55%,#236a76 100%);color:var(--white)}
.newsletter-label{position:absolute;left:256px;top:57px;display:flex;align-items:center;gap:12px;font-size:16px;text-transform:uppercase}
.newsletter-input{position:absolute;left:589px;top:56px;width:288px;height:24px;background:#e9eef0;color:#9aa;font-size:8px;display:flex;align-items:center;justify-content:center;text-transform:uppercase}
.newsletter-send{position:absolute;left:877px;top:56px;width:67px;height:24px;background:var(--teal-dark);border:1px solid #cfe;font-size:8px;display:flex;align-items:center;justify-content:center;text-transform:uppercase}
.footer-rule{position:absolute;left:160px;width:880px;height:1px;background:rgba(255,255,255,.35)}
.footer-brand{position:absolute;left:160px;top:190px;font-family:"Great Vibes",cursive;font-size:52px;line-height:1}
.footer-about{position:absolute;left:160px;top:245px;width:200px;font-size:10px;line-height:15px}
.footer-about p+p{margin-top:14px}
.learn-more{position:absolute;font-size:9px;text-transform:uppercase;text-decoration:underline}
.footer-heading{position:absolute;font-size:16px;text-transform:uppercase}
.post{position:absolute;left:386px;width:200px;display:flex;gap:15px}
.post-thumb{width:36px;height:34px;flex:none;border:2px solid var(--white)}
.post p{font-size:9.5px;line-height:13px}
.contact-box{position:absolute;left:611px;top:168px;width:429px;height:289px;border:1px solid rgba(255,255,255,.25);background:rgba(255,255,255,.06)}
.contact-box h4{position:absolute;left:0;top:26px;width:100%;text-align:center;font-size:14px;font-weight:400;text-transform:uppercase}
.contact-box .lead{position:absolute;left:0;top:49px;width:100%;text-align:center;font-size:10px}
.field{position:absolute;left:52px;width:323px;border:1px solid rgba(255,255,255,.7);font-size:8px;color:rgba(255,255,255,.6);display:flex;justify-content:center;padding-top:4px;text-transform:uppercase}
.contact-send{position:absolute;left:193px;top:247px;width:42px;height:22px;border:1px solid var(--white);font-size:9px;display:flex;align-items:center;justify-content:center}
.social{position:absolute;left:170px;top:2500px;width:860px;display:flex;justify-content:space-between}
.social-dot{width:20px;height:20px;border-radius:50%;border:2px solid rgba(255,255,255,.85)}
.copyright{position:absolute;left:173px;top:586px;font-size:11px}
.legal-links{position:absolute;left:739px;top:586px;font-size:11px;display:flex;gap:14px}
.legal-links span.sep{opacity:.8}
</style>
</head>
<body>

<header class="site-header">
  <div class="brand">Velmo</div>
  <nav class="main-nav">
    <div class="nav-item active">
      <svg viewBox="0 0 28 28"><circle cx="14" cy="14" r="13" fill="#fff"/><path d="M8 15 14 9l6 6v5h-4v-3h-4v3H8z" fill="#1e6f7c"/></svg>Home
    </div>
    <div class="nav-item">
      <svg viewBox="0 0 28 28"><circle cx="14" cy="14" r="13" fill="#2a2a2a"/><rect x="9" y="8" width="10" height="12" fill="none" stroke="#fff" stroke-width="1.6"/></svg>Pages
    </div>
    <div class="nav-item">
      <svg viewBox="0 0 28 28"><circle cx="14" cy="14" r="13" fill="#2a2a2a"/><rect x="8" y="10" width="12" height="9" rx="1" fill="none" stroke="#fff" stroke-width="1.6"/><path d="M11 10V8h6v2" stroke="#fff" stroke-width="1.6" fill="none"/></svg>Portfolio
    </div>
    <div class="nav-item">
      <svg viewBox="0 0 28 28"><circle cx="14" cy="14" r="13" fill="#2a2a2a"/><path d="M9 19l1-4 8-8 3 3-8 8z" fill="none" stroke="#fff" stroke-width="1.6"/></svg>Blog
    </div>
    <div class="nav-item">
      <svg viewBox="0 0 28 28"><circle cx="14" cy="14" r="13" fill="#2a2a2a"/><rect x="8" y="10" width="12" height="8" fill="none" stroke="#fff" stroke-width="1.6"/><path d="M8 10l6 5 6-5" fill="none" stroke="#fff" stroke-width="1.6"/></svg>Contact
    </div>
    <div class="nav-search">
      <svg width="26" height="26" viewBox="0 0 26 26"><circle cx="13" cy="13" r="12" fill="none" stroke="#2a2a2a" stroke-width="1.4"/><circle cx="12" cy="12" r="4" fill="none" stroke="#2a2a2a" stroke-width="1.6"/><path d="M15 15l3 3" stroke="#2a2a2a" stroke-width="1.8"/></svg>
    </div>
  </nav>
</header>

<section class="hero" role="img" aria-label="Smiling businesswoman in a grey suit in a bright office with colleagues softly blurred behind her">
  <h1 class="hero-title"><span class="accent">We</span> Will show you<br>The Way To <span class="accent">Success</span></h1>
  <p class="hero-sub">Give us a chance and we will prove our efficiency!</p>
  <div class="hero-btn">Resquest For Quote &gt;</div>
  <div class="hero-arrow" style="left:0"><svg width="14" height="20" viewBox="0 0 14 20"><path d="M11 2 3 10l8 8" fill="none" stroke="#fff" stroke-width="2.5"/></svg></div>
  <div class="hero-arrow" style="left:1152px"><svg width="14" height="20" viewBox="0 0 14 20"><path d="M3 2l8 8-8 8" fill="none" stroke="#fff" stroke-width="2.5"/></svg></div>
  <div class="hero-progress"></div>
</section>

<!-- services -->
<h2 class="section-title" style="top:644px">Services</h2>
<div class="divider" style="top:701px"></div>
<div class="divider-badge" style="top:688px"><svg width="14" height="14" viewBox="0 0 14 14"><circle cx="7" cy="7" r="4" fill="none" stroke="#fff" stroke-width="2"/><circle cx="7" cy="7" r="1.3" fill="#fff"/></svg></div>

<div class="service" style="left:150px">
  <div class="service-icon"><svg width="34" height="34" viewBox="0 0 34 34"><circle cx="17" cy="17" r="14" fill="none" stroke="#1e6f7c" stroke-width="3"/><path d="M17 9v9h7" fill="none" stroke="#1e6f7c" stroke-width="3"/></svg></div>
  <h3>24 Hours Services</h3>
  <p>Our advisors stay ready to review your request at any hour of any day.</p>
</div>
<div class="service" style="left:377px">
  <div class="service-icon"><svg width="36" height="34" viewBox="0 0 36 34"><rect x="13" y="3" width="10" height="8" fill="#1e6f7c"/><rect x="2" y="23" width="9" height="8" fill="#1e6f7c"/><rect x="13.5" y="23" width="9" height="8" fill="#1e6f7c"/><rect x="25" y="23" width="9" height="8" fill="#1e6f7c"/><path d="M18 11v12M6.5 23v-6h23v6" fill="none" stroke="#1e6f7c" stroke-width="2.2"/></svg></div>
  <h3>Tell Us What You Need Done</h3>
  <p>Post your brief once and let qualified advisors come to you with a pitch.</p>
</div>
<div class="service" style="left:603px">
  <div class="service-icon filled"><svg width="34" height="34" viewBox="0 0 34 34"><path d="M26 5c-7 1-12 6-15 12l6 6c6-3 11-8 12-15z" fill="#fff"/><path d="M11 17l-5 1 3-5 5-1zM17 23l-1 5 5-3 1-5z" fill="#fff"/><path d="M9 25l-3 3" stroke="#fff" stroke-width="2.5"/></svg></div>
  <h3>Get Competitive Quotes</h3>
  <p>Compare fees and terms side by side before you choose the right partner.</p>
</div>
<div class="service" style="left:828px">
  <div class="service-icon"><svg width="34" height="34" viewBox="0 0 34 34"><path d="M6 27h22M6 22h22M8 17h18l1 5M10 12l16 4M13 7l14 7" fill="none" stroke="#1e6f7c" stroke-width="3"/></svg></div>
  <h3>Hire The Best Business</h3>
  <p>Review each advisor profile in full and hire the one that fits best.</p>
</div>

<!-- stats -->
<section class="stats" role="img" aria-label="Wide glacier and snowy mountain range tinted teal">
  <div class="stat" style="left:104px"><strong>150</strong><span>Employess</span></div>
  <div class="stat" style="left:292px"><strong>365</strong><span>Days Worked</span></div>
  <div class="stat" style="left:485px"><strong>100</strong><span>Happy Clients</span></div>
  <div class="stat" style="left:693px"><strong>150</strong><span>Clients Added</span></div>
  <div class="stat" style="left:888px"><strong>50</strong><span>Awards Won</span></div>
</section>

<!-- recent work -->
<h2 class="section-title" style="top:1184px">Recent Work</h2>
<div class="divider" style="top:1243px"></div>
<div class="divider-badge" style="top:1230px"><svg width="14" height="14" viewBox="0 0 14 14"><rect x="2" y="3" width="10" height="8" rx="1" fill="#fff"/><path d="M4 6h6M4 8h6" stroke="#1e6f7c" stroke-width="1"/></svg></div>

<div class="work-tile" style="left:160px;top:1310px;background:linear-gradient(135deg,#8a7a6c,#c9c2b8 50%,#5d6670)" role="img" aria-label="Team gathered around a laptop reviewing charts"></div>
<div class="work-tile" style="left:461px;top:1310px;background:linear-gradient(135deg,#dfe3e6,#9aa8b3 55%,#4a5561)" role="img" aria-label="Two businessmen in suits talking in an office"></div>
<div class="work-tile" style="left:765px;top:1310px;background:linear-gradient(135deg,#e8ecef,#8c9299 55%,#2e3338)" role="img" aria-label="Business partners shaking hands across a table"></div>
<div class="work-tile" style="left:160px;top:1514px;background:linear-gradient(135deg,#a49686,#d8d2c8 50%,#6a6f74)" role="img" aria-label="Colleagues discussing documents at a meeting"></div>
<div class="work-tile" style="left:461px;top:1514px;background:linear-gradient(135deg,#6b5a4c,#b7a08a 50%,#3e3a36)" role="img" aria-label="Smiling businessman at a desk">
  <div class="work-overlay"></div>
  <svg class="zoom" width="34" height="34" viewBox="0 0 34 34"><circle cx="14" cy="14" r="10" fill="none" stroke="#fff" stroke-width="2.5"/><path d="M21 21l9 9M10 14h8M14 10v8" stroke="#fff" stroke-width="2.5"/></svg>
  <div class="work-label">Project Name Here</div>
</div>
<div class="work-tile" style="left:765px;top:1514px;background:linear-gradient(135deg,#d7dcdf,#9aa2a8 50%,#3d4348)" role="img" aria-label="Business people seated in a bright lobby"></div>

<!-- testimonials -->
<section class="testimonials on-dark" role="img" aria-label="Skyline of a domed mosque with minarets and birds, tinted teal">
  <h2 class="section-title" style="top:56px">What Client Says</h2>
  <div class="divider" style="top:114px;background:rgba(255,255,255,.7)"></div>
  <div class="divider-badge" style="top:101px;background:#4a95a1;border:1px solid #fff"><svg width="12" height="12" viewBox="0 0 12 12"><path d="M2 10l1-3 5-5 2 2-5 5z" fill="#fff"/></svg></div>
  <svg class="quote-arrow" style="left:160px" width="14" height="22" viewBox="0 0 14 22"><path d="M11 3 3 11l8 8" fill="none" stroke="#fff" stroke-width="3"/></svg>
  <div class="avatar"></div>
  <p class="quote">“Posting our funding brief took minutes, and within a week we had several strong pitches from advisors who clearly understood our sector. Keeping our name private until we were ready made the whole process feel safe. We chose our advisor from their profile and closed the deal sooner than we expected.”</p>
  <svg class="quote-arrow" style="left:1024px" width="14" height="22" viewBox="0 0 14 22"><path d="M3 3l8 8-8 8" fill="none" stroke="#fff" stroke-width="3"/></svg>
  <div class="dots"><span class="dot hollow"></span><span class="dot"></span><span class="dot"></span><span class="dot"></span></div>
</section>

<!-- clients -->
<h2 class="section-title" style="top:2312px">Our Clients</h2>
<div class="divider" style="top:2367px"></div>
<div class="divider-badge" style="top:2354px"><svg width="12" height="14" viewBox="0 0 12 14"><path d="M6 1C3 5 2 7 2 9a4 4 0 0 0 8 0c0-2-1-4-4-8z" fill="#fff"/></svg></div>

<svg class="client-arrow" style="left:160px" width="16" height="28" viewBox="0 0 16 28"><path d="M13 2 3 14l10 12" fill="none" stroke="#b5b5b5" stroke-width="3"/></svg>
<div class="client" style="left:258px"><span class="client-mark"></span>Lumora</div>
<div class="client" style="left:448px"><span class="client-mark"></span>Pexaro</div>
<div class="client" style="left:633px">Ostrivo</div>
<div class="client" style="left:816px"><span class="client-mark"></span>Teldra</div>
<svg class="client-arrow" style="left:1024px" width="16" height="28" viewBox="0 0 16 28"><path d="M3 2l10 12L3 26" fill="none" stroke="#b5b5b5" stroke-width="3"/></svg>

<!-- footer -->
<footer class="site-footer" role="img" aria-label="Lakeside mountains at dusk tinted teal behind the footer">
  <div class="newsletter-label">
    <svg width="22" height="20" viewBox="0 0 22 20"><rect x="1" y="4" width="14" height="14" rx="2" fill="none" stroke="#fff" stroke-width="2"/><path d="M8 12l1-3 9-8 3 3-9 8z" fill="#fff"/></svg>
    Subscribe to our newsletter
  </div>
  <div class="newsletter-input">Enter your email</div>
  <div class="newsletter-send">Send</div>
  <div class="footer-rule" style="top:134px"></div>

  <div class="footer-brand">Velmo</div>
  <div class="footer-about">
    <p>Velmo connects growing companies with trusted debt, legal and accounting advisors who pitch for the work you post.</p>
    <p>Clients stay anonymous behind a client number while they compare proposals and choose the right advisor.</p>
  </div>
  <div class="learn-more" style="left:160px;top:414px">Learn more</div>

  <div class="footer-heading" style="left:386px;top:195px">Recent Post</div>
  <div class="post" style="top:238px"><span class="post-thumb" style="background:linear-gradient(135deg,#d9a06a,#7a4f3a)"></span><p>Preparing your business for a debt raise<br>December 13, 2013</p></div>
  <div class="post" style="top:292px"><span class="post-thumb" style="background:linear-gradient(135deg,#9fc1d6,#3f6f8c)"></span><p>What advisors look for in a client brief<br>December 13, 2013</p></div>
  <div class="post" style="top:349px"><span class="post-thumb" style="background:linear-gradient(135deg,#f2b35c,#6e3a22)"></span><p>Choosing between bank and private lenders<br>December 13, 2013</p></div>
  <div class="learn-more" style="left:437px;top:414px">Learn more</div>

  <div class="contact-box">
    <h4>Get in touch</h4>
    <p class="lead">We would love to hear from you</p>
    <div class="field" style="top:100px;height:26px">Name</div>
    <div class="field" style="top:137px;height:24px">Email</div>
    <div class="field" style="top:165px;height:70px">Message</div>
    <div class="contact-send">Send</div>
  </div>

  <div class="social" style="top:500px">
    <span class="social-dot"></span><span class="social-dot"></span><span class="social-dot"></span><span class="social-dot"></span><span class="social-dot"></span>
    <span class="social-dot"></span><span class="social-dot"></span><span class="social-dot"></span><span class="social-dot"></span><span class="social-dot"></span>
    <span class="social-dot"></span><span class="social-dot"></span>
  </div>
  <div class="footer-rule" style="top:560px"></div>
  <div class="copyright">Copyright @ 2014,All Rights Reserved</div>
  <div class="legal-links"><span>Home</span><span class="sep">|</span><span>About Us</span><span class="sep">|</span><span>Sitemap</span><span class="sep">|</span><span>Contact Us</span></div>
</footer>

</body>
</html>
```